Sudden Tides "Lantern Road" New Single Cover

Create cover artwork for the band Sudden Tides' new single "Lantern Road" being released early 2020. Style, font and graphics to be consistent with band's previous releases and overall brand identity. Visit www.suddentidesband.example and our Spotify page https://music.example.net/artist/7QzWpLx3RtVnKd8e2YbHcJ?si=MUrTgKa4PLe7skvWq2AmZd to view our previous releases and overall brand identity. Some examples attached as well. We are looking for someone to work with on future projects as well.

Lyrics are here: https://docs.example.org/document/d/3KTp9wrn_2ZQa8eXb4Lo_fimH7C5m83Jz4Pd70hrtVcA/edit

Music is here: https://audiostream.example.com/suddentides/lantern-road/s-pzkwa

Font styles to use
Sans Serif

Colors

Designer to choose colors to be used in the design.

Requirements
Must have
• Must be consistent with current brand identity and with prior album / single art.

```html
<!DOCTYPE html>
<html lang="en">
<head>
<meta charset="utf-8">
<title>Sudden Tides – Lantern Road</title>
<link rel="stylesheet" href="https://fonts.googleapis.com/css2?family=Montserrat:wght@300;700&display=swap">
<style>
  :root {
    --paper: #f1f1f1;
    --paper-shade: #e6e6e8;
    --ink: #2a2728;
    --stage: #4fe6a2;
    --stage-deep: #3fdf8f;
  }
  html, body {
    margin: 0;
    padding: 0;
    width: 1200px;
    height: 2400px;
    overflow: hidden;
    background: var(--paper);
  }
  .canvas {
    position: relative;
    width: 1200px;
    height: 2400px;
  }
  .cover {
    position: absolute;
    width: 1200px;
    height: 1200px;
    background: var(--paper);
    font-family: "Montserrat", sans-serif;
    color: var(--ink);
    overflow: hidden;
  }
  .cover--main {
    left: 0;
    top: 0;
  }
  .cover--display {
    left: 219px;
    top: 1386px;
    transform: scale(0.645);
    transform-origin: 0 0;
    background: var(--paper-shade);
  }
  .single-title {
    position: absolute;
    top: 183px;
    left: 0;
    width: 100%;
    margin: 0;
    text-align: center;
    font-weight: 700;
    font-size: 46px;
    line-height: 56px;
    letter-spacing: 0;
    text-transform: uppercase;
  }
  .artwork {
    position: absolute;
    left: 140px;
    top: 321px;
    width: 920px;
    height: 574px;
  }
  .band-name {
    position: absolute;
    top: 992px;
    left: 0;
    width: 100%;
    margin: 0;
    text-align: center;
    font-weight: 300;
    font-size: 54px;
    line-height: 56px;
    letter-spacing: 5px;
    text-transform: uppercase;
  }
  .band-name span { display: block; }
  .stage {
    position: absolute;
    left: 0;
    top: 1200px;
    width: 1200px;
    height: 1200px;
    background: linear-gradient(180deg, var(--stage) 0%, var(--stage-deep) 55%, var(--stage) 100%);
  }
</style>
</head>
<body>
<main class="canvas">
  <section class="cover cover--main">
    <h1 class="single-title">Lantern Road</h1>
    <svg class="artwork" viewBox="0 0 920 574" role="img" aria-label="Illustration of a black heart shattering into flying shards toward the right">
      <defs>
        <linearGradient id="shatter-tone-a" x1="0" y1="0" x2="1" y2="0">
          <stop offset="0" stop-color="#2a2728"/>
          <stop offset="0.45" stop-color="#2a2728"/>
          <stop offset="1" stop-color="#2a2728" stop-opacity="0"/>
        </linearGradient>
      </defs>
      <rect x="0" y="40" width="920" height="520" rx="200" fill="url(#shatter-tone-a)"/>
    </svg>
    <h2 class="band-name"><span>Sudden</span><span>Tides</span></h2>
  </section>

  <div class="stage"></div>

  <section class="cover cover--display">
    <h1 class="single-title">Lantern Road</h1>
    <svg class="artwork" viewBox="0 0 920 574" role="img" aria-label="Illustration of a black heart shattering into flying shards toward the right">
      <defs>
        <linearGradient id="shatter-tone-b" x1="0" y1="0" x2="1" y2="0">
          <stop offset="0" stop-color="#2a2728"/>
          <stop offset="0.45" stop-color="#2a2728"/>
          <stop offset="1" stop-color="#2a2728" stop-opacity="0"/>
        </linearGradient>
      </defs>
      <rect x="0" y="40" width="920" height="520" rx="200" fill="url(#shatter-tone-b)"/>
    </svg>
    <h2 class="band-name"><span>Sudden</span><span>Tides</span></h2>
  </section>
</main>
</body>
</html>
```